Website improvements and Adding Functionalities at https://quorin.net/tamberly

1.Search functionality
2.Payment process functionality
3. Application configuration
4. Registration functionality activation
5. Chat functionality
6.Language switching functionality (Portuguese & French)
7.Bespoke interactive modules
8. Automated web scraping and data synchronisation mechanisms
9. News Page
10.Webinar facilities
11. Basic SEO optimisation
12. Speed and performance optimisation
13. Security configuration
14. Google Analytics integration
15. Cross-browser and mobile testing
16. Website deployment and launch support

Target Market(s)

My target markets are companies, investors, suppliers and professionals with an interest in the Mozambican oil and gas sector

Industry/Entity Type

Oil and Gas

Coding

Coded - Design and coding required

Number of Pages Required

1 page

Requirements
Must have
• Improve the existing page at https://quorin.net/tamberly and add the following features to it: 1. Search functionality 2. Payment process functionality 3. Application configuration 4. Activation of registration functionality 5. Chat functionality 6. Language switching functionality (Portuguese & French) 7. Bespoke interactive modules 8. Automated web scraping and data synchronisation mechanisms 9. News Page

```html
<!DOCTYPE html>
<html lang="en">
<head>
<meta charset="utf-8">
<title>Tamberly – Mozambique Oil &amp; Gas Intelligence</title>
<link href="https://fonts.googleapis.com/css2?family=Rajdhani:wght@400;500;600;700&display=swap" rel="stylesheet">
<style>
:root{
  --navy:#141a33;
  --navy-deep:#0c1730;
  --orange:#ef4a24;
  --white:#ffffff;
  --grey-line:#c9c9c9;
  --text-grey:#555a66;
  --beige:#ebe5d9;
}
*{box-sizing:border-box;margin:0;padding:0}
html,body{width:1200px;height:4732px;overflow:hidden}
body{font-family:"Rajdhani",sans-serif;color:var(--navy);position:relative;
  background:linear-gradient(to bottom,#fff 0,#fff 3050px,#f3efe8 3300px,var(--beige) 4012px)}
.abs{position:absolute}
.btn{display:inline-flex;align-items:center;justify-content:center;font-weight:700;text-transform:uppercase;letter-spacing:.5px;border-radius:4px;font-size:18px}
.btn-navy{background:var(--navy);color:#fff}
.btn-orange{background:var(--orange);color:#fff}
.btn-white{background:#fff;color:var(--orange)}

/* header */
.site-header{left:0;top:0;width:1200px;height:138px;background:#fff}
.brand{left:140px;top:40px;display:flex;align-items:center;gap:12px;font-weight:700;font-size:26px;color:var(--navy)}
.brand-dot{width:40px;height:40px;border-radius:50%;background:var(--orange)}
.search{left:436px;top:44px;width:190px;height:42px;border:1px solid #bbb;border-radius:4px;font-size:15px;color:#777;padding:0 16px;display:flex;align-items:center;justify-content:space-between}
.header-register{left:636px;top:42px;width:174px;height:46px}
.header-contact{left:820px;top:42px;width:174px;height:46px}
.lang{left:1012px;top:54px;font-size:16px;font-weight:700}
.main-nav{left:0;top:138px;width:1200px;height:50px;background:linear-gradient(to bottom,#f47d5d,var(--orange));display:flex;align-items:center;padding-left:127px}
.main-nav a{color:#fff;text-decoration:none;font-weight:700;font-size:14.5px;text-transform:uppercase;padding:0 12px;height:50px;display:flex;align-items:center}
.main-nav a.active{background:var(--navy)}

/* hero */
.hero-photo{left:0;top:188px;width:1200px;height:767px;background:linear-gradient(to bottom,#3a4150 0%,#7a5a45 35%,#c2743a 55%,#4b3a34 100%)}
.hero-title{left:0;top:393px;width:1200px;text-align:center;color:#fff;font-size:46px;font-weight:700;line-height:54px;text-transform:uppercase}
.hero-lead{left:220px;top:533px;width:760px;text-align:center;color:#fff;font-size:19px;font-weight:600;line-height:29px}
.hero-register{left:400px;top:665px;width:196px;height:46px}
.hero-contact{left:606px;top:665px;width:196px;height:46px}
.dots{left:560px;top:798px;display:flex;gap:17px}
.dots span{width:15px;height:15px;border-radius:50%;background:#fff}
.dots span:first-child{background:#f5a623}

/* intro */
.intro-shape{left:0;top:820px}
.intro-image{left:200px;top:974px;width:348px;height:432px;border-radius:174px 174px 0 0;background:linear-gradient(to bottom,#f29a3a,#b4471c 55%,#2a1a18)}
.intro-text{left:597px;top:1015px;width:398px;color:#fff}
.intro-text h2{font-size:44px;font-weight:700;line-height:52px;text-transform:uppercase;margin-bottom:20px}
.intro-text p{font-size:17px;line-height:29px;text-align:justify;font-weight:500}
.intro-text .btn{margin-top:30px;width:174px;height:44px;font-size:17px}

/* access */
.section-title{left:0;width:1200px;text-align:center;font-size:44px;font-weight:700;text-transform:uppercase}
.section-title em{font-style:normal;color:var(--orange)}
.card{width:284px;height:416px;border:2px solid var(--grey-line);border-bottom-width:1px;border-radius:142px 142px 0 0;background:#fff;text-align:center;overflow:hidden}
.card.featured{background:var(--orange);border-color:var(--orange)}
.card .pic{width:232px;height:232px;border-radius:50%;margin:18px auto 0}
.card h3{font-size:18px;font-weight:700;line-height:27px;text-transform:uppercase;margin:22px 20px 8px}
.card p{font-size:14.5px;line-height:22px;color:var(--text-grey);margin:0 18px}
.card.featured h3,.card.featured p{color:#fff}
.card .corner{position:absolute;right:0;bottom:0;width:46px;height:46px;border-radius:46px 0 0 0;background:var(--orange);display:flex;align-items:center;justify-content:center;padding:8px 0 0 8px}
.card.featured .corner{background:#fff}
.view-more{left:513px;top:2630px;width:174px;height:44px;background:var(--navy-deep);color:#fff;font-size:17px}

/* how */
.how-image{left:200px;top:2876px;width:348px;height:432px;border-radius:174px 174px 0 0;background:linear-gradient(to bottom,#d98a3d,#6b3a22 50%,#15192a)}
.how-text{left:597px;top:2905px;width:398px;color:#fff}
.how-text h2{font-size:44px;font-weight:700;line-height:52px;text-transform:uppercase;margin-bottom:18px}
.how-text h2 em{font-style:normal;color:var(--orange)}
.how-text p{font-size:17px;line-height:29px;text-align:justify;font-weight:500}
.how-text .btn{margin-top:30px;width:174px;height:44px;font-size:17px}

/* unique */
.step-num{font-size:150px;font-weight:700;line-height:1}
.step{width:270px;height:270px;border-radius:50%;border:4px dashed var(--navy);text-align:center;display:flex;flex-direction:column;justify-content:center;padding:0 30px 0 62px}
.step.mid{border-color:var(--orange)}
.step h4{font-size:17.5px;font-weight:700;line-height:24px;text-transform:uppercase;margin-bottom:8px}
.step p{font-size:14.5px;line-height:22px;color:var(--text-grey)}

/* cta */
.cta-band{left:0;top:4012px;width:1200px;height:552px;background:linear-gradient(to bottom,#f2633a,var(--orange))}
.cta-mark{left:750px;top:4080px;width:360px;height:360px;border-radius:50%;background:rgba(20,26,51,.12)}
.cta-title{left:145px;top:4110px;width:560px;color:#fff;font-size:46px;font-weight:700;line-height:58px;text-transform:uppercase}
.cta-lead{left:145px;top:4297px;width:500px;color:#fff;font-size:21px;line-height:35px}
.cta-register{left:146px;top:4428px;width:174px;height:44px;font-size:17px}
.cta-contact{left:330px;top:4428px;width:174px;height:44px;font-size:17px}

/* footer */
.footer{left:0;top:4564px;width:1200px;height:168px;background:var(--navy)}
.footer-links{left:145px;top:4604px;display:flex;gap:18px;align-items:center;color:#fff;font-size:15px;font-weight:600}
.footer-links .sep{width:1px;height:18px;background:#555c7a}
.pay{border:1px solid #fff;border-radius:3px;padding:1px 8px;font-size:13px}
.copyright{left:145px;top:4658px;color:#fff;font-size:16px}
</style>
</head>
<body>

<header class="abs site-header">
  <div class="abs brand"><span class="brand-dot"></span>Tamberly Co</div>
  <div class="abs search">Search
    <svg width="16" height="16" viewBox="0 0 16 16"><circle cx="6.5" cy="6.5" r="5" fill="none" stroke="#333" stroke-width="2"/><line x1="10" y1="10" x2="15" y2="15" stroke="#333" stroke-width="2"/></svg>
  </div>
  <a class="abs btn btn-navy header-register">Register now</a>
  <a class="abs btn btn-orange header-contact">Contact us</a>
  <div class="abs lang">EN ▾</div>
</header>
<nav class="abs main-nav">
  <a class="active">Home</a><a>Industry insights</a><a>Oil &amp; gas opportunities</a><a>Supplier &amp; company network</a><a>Legal framework</a><a>News</a>
</nav>

<section class="abs hero-photo" role="img" aria-label="Pipelines and refinery towers under a sunset sky"></section>
<h1 class="abs hero-title">Access Mozambique’s oil &amp; gas industry<br>intelligence in one platform</h1>
<p class="abs hero-lead">Tamberly is a modern online connection and consulting platform designed to facilitate access to the Mozambican Oil and Gas industry through premium industry insights, supplier information, tenders, legal frameworks, and strategic project data.</p>
<a class="abs btn btn-navy hero-register">Register now</a>
<a class="abs btn btn-orange hero-contact">Contact us</a>
<div class="abs dots"><span></span><span></span><span></span></div>

<svg class="abs intro-shape" width="1200" height="680" viewBox="0 820 1200 680">
  <defs><linearGradient id="introGrad" x1="0" y1="0" x2="0" y2="1"><stop offset="0" stop-color="#f57a55"/><stop offset="1" stop-color="#ee4725"/></linearGradient></defs>
  <path d="M0,820 C80,880 170,930 260,960 L0,960 Z" fill="#fff"/>
  <path d="M1200,820 C1120,880 1030,930 940,960 L1200,960 Z" fill="#fff"/>
  <path d="M0,955 L1200,955 L1200,1500 L0,1500 Z" fill="#fff"/>
  <path d="M145,1000 C320,890 470,862 600,862 C730,862 880,890 1055,1000 L1055,1480 L145,1480 Z" fill="url(#introGrad)"/>
</svg>
<div class="abs intro-image" role="img" aria-label="Offshore platform at sunset with pipeline"></div>
<div class="abs intro-text">
  <h2>What is Tamberly?</h2>
  <p>Tamberly is a unique online platform built to connect businesses, investors, suppliers, and professionals with valuable information about the Mozambican Oil &amp; Gas sector.Through a secure digital paywall system, users gain access to organized, up-to-date, and carefully selected industry information that supports better decision-making, market understanding, and business opportunities within Mozambique's growing hydrocarbons industry.</p>
  <a class="btn btn-navy">Read more</a>
</div>

<h2 class="abs section-title" style="top:1590px">What you <em>will access</em></h2>

<div class="abs card" style="left:145px;top:1705px">
  <div class="pic" role="img" aria-label="Hand holding a digital oil price cycle graphic" style="background:radial-gradient(circle,#2e5a7a,#0d1a2e)"></div>
  <h3>Hydrocarbon<br>industry information</h3><p>General information and insights about Mozambique's oil and gas sector.</p>
  <div class="corner"><svg width="18" height="14" viewBox="0 0 18 14"><path d="M0 7H16M10 1L16 7L10 13" fill="none" stroke="#fff" stroke-width="2"/></svg></div>
</div>
<div class="abs card featured" style="left:458px;top:1705px">
  <div class="pic" role="img" aria-label="Engineer with laptop at a gas facility" style="background:linear-gradient(#bcd3e8,#e9954a)"></div>
  <h3>Main gas projects</h3><p>Details about major gas and energy projects operating in Mozambique.</p>
  <div class="corner"><svg width="18" height="14" viewBox="0 0 18 14"><path d="M0 7H16M10 1L16 7L10 13" fill="none" stroke="#ef4a24" stroke-width="2"/></svg></div>
</div>
<div class="abs card" style="left:770px;top:1705px">
  <div class="pic" role="img" aria-label="Business network gear diagram" style="background:radial-gradient(circle,#3a5873,#1a2a3c)"></div>
  <h3>Supplier &amp; company<br>database</h3><p>Mozambican companies capable of meeting Level 3 supply requirements.</p>
  <div class="corner"><svg width="18" height="14" viewBox="0 0 18 14"><path d="M0 7H16M10 1L16 7L10 13" fill="none" stroke="#fff" stroke-width="2"/></svg></div>
</div>
<div class="abs card" style="left:145px;top:2161px">
  <div class="pic" role="img" aria-label="Glowing tools gear above an open hand" style="background:radial-gradient(circle,#e8823a,#152033 70%)"></div>
  <h3>Industry contacts</h3><p>Key contacts from NOCs, Operators, EPCs, and Second-Tier Suppliers.</p>
  <div class="corner"><svg width="18" height="14" viewBox="0 0 18 14"><path d="M0 7H16M10 1L16 7L10 13" fill="none" stroke="#fff" stroke-width="2"/></svg></div>
</div>
<div class="abs card" style="left:458px;top:2161px">
  <div class="pic" role="img" aria-label="Digital request for proposal document between vendors" style="background:radial-gradient(circle,#4a4f8a,#121a35)"></div>
  <h3>Tender<br>opportunities</h3><p>Short, medium, and long-term tenders within the industry.</p>
  <div class="corner"><svg width="18" height="14" viewBox="0 0 18 14"><path d="M0 7H16M10 1L16 7L10 13" fill="none" stroke="#fff" stroke-width="2"/></svg></div>
</div>
<div class="abs card" style="left:770px;top:2161px">
  <div class="pic" role="img" aria-label="Stacked wooden blocks about ownership and responsibility" style="background:linear-gradient(#3a2a22,#c89a6a)"></div>
  <h3>Ownership &amp; access</h3><p>Information related to hydrocarbon reserves and sector participation.</p>
  <div class="corner"><svg width="18" height="14" viewBox="0 0 18 14"><path d="M0 7H16M10 1L16 7L10 13" fill="none" stroke="#fff" stroke-width="2"/></svg></div>
</div>
<a class="abs btn view-more">View more</a>

<svg class="abs" style="left:0;top:2757px" width="1200" height="626" viewBox="0 0 1200 626">
  <defs><linearGradient id="howGrad" x1="0" y1="0" x2="0" y2="1"><stop offset="0" stop-color="#0d3250"/><stop offset="1" stop-color="#050d1c"/></linearGradient></defs>
  <path d="M145,148 C320,40 470,0 600,0 C730,0 880,40 1055,148 L1055,625 L145,625 Z" fill="url(#howGrad)"/>
</svg>
<div class="abs how-image" role="img" aria-label="Offshore rig at dusk with security and data icons"></div>
<div class="abs how-text">
  <h2>How the<br><em>platform works</em></h2>
  <p>The platform operates through a secure automated payment system that grants registered users access to premium and exclusive content. By subscribing, users receive organized industry intelligence designed to save time, improve market access, and support strategic business growth within Mozambique's energy sector.</p>
  <a class="btn btn-orange">Read more</a>
</div>

<h2 class="abs section-title" style="top:3487px">Why Tamberly <em>is unique</em></h2>
<div class="abs step" style="left:110px;top:3603px"><h4>Up-to-date industry intelligence</h4><p>Receive frequent updates about developments in Mozambique's Oil &amp; Gas sector.</p></div>
<div class="abs step-num" style="left:88px;top:3666px">1</div>
<svg class="abs" style="left:378px;top:3700px" width="80" height="80"><path d="M0,0 L80,40 L0,80 L22,40 Z" fill="var(--navy)"/></svg>
<div class="abs step mid" style="left:452px;top:3603px"><h4>High-quality curated information</h4><p>Access carefully selected and synthesized information tailored to industry stakeholders.</p></div>
<div class="abs step-num" style="left:440px;top:3666px;color:var(--orange)">2</div>
<svg class="abs" style="left:730px;top:3700px" width="80" height="80"><path d="M0,0 L80,40 L0,80 L22,40 Z" fill="var(--orange)"/></svg>
<div class="abs step" style="left:812px;top:3603px"><h4>Time-saving access</h4><p>Avoid spending hours searching through scattered online sources with organized and accessible content in one platform.</p></div>
<div class="abs step-num" style="left:790px;top:3666px">3</div>
<svg class="abs" style="left:1090px;top:3700px" width="80" height="80"><path d="M0,0 L80,40 L0,80 L22,40 Z" fill="var(--navy)"/></svg>

<section class="abs cta-band"></section>
<div class="abs cta-mark"></div>
<h2 class="abs cta-title">Start exploring Mozambique’s oil &amp; gas opportunities</h2>
<p class="abs cta-lead">Register today to access premium industry information, supplier networks, tenders, and strategic market insights through Tamberly.</p>
<a class="abs btn btn-navy cta-register">Register now</a>
<a class="abs btn btn-white cta-contact">Contact us</a>

<footer class="abs footer"></footer>
<div class="abs footer-links">
  <span>Gallery</span><span>Feed</span><span>Pronet</span><span class="sep"></span>
  <span class="pay">Cardo</span><span class="pay">Linq</span><span class="pay">Banquo</span><span class="pay">Tallis</span><span class="pay">Orvo</span>
</div>
<div class="abs copyright">© 2026 by Tamberly Co. All Rights Reserved &nbsp;|&nbsp; Privacy Policy &nbsp;|&nbsp; Terms of Use</div>

</body>
</html>
```